Copperleaf Motorized Shade Business Card

Hello, we've had our logo made. Now we are looking for a clean and cool looking business card. One side can just be the logo with any design elements that might look good with it. The other side will be Name, Phone Number and Email. There will not be an address on the card.

```html
<!DOCTYPE html>
<html lang="en">
<head>
<meta charset="UTF-8">
<title>Copperleaf Motorized Shade Business Card</title>
<link rel="stylesheet" href="https://fonts.googleapis.com/css2?family=Roboto:wght@500;700&display=swap">
<style>
  :root {
    --navy: #013a70;
    --blue: #0067b1;
    --sky: #00aeef;
    --sun: #ffc20e;
    --paper: #fbfbfb;
    --page: #ffffff;
    --white: #ffffff;
  }
  * { margin: 0; padding: 0; box-sizing: border-box; }
  html, body {
    width: 1200px; height: 1200px; overflow: hidden;
    background: var(--page);
    font-family: "Roboto", Arial, sans-serif;
  }
  .card {
    position: absolute; left: 166px; width: 876px; height: 535px;
  }
  .card-front {
    top: 51px;
    background: linear-gradient(135deg, #ffffff 0%, var(--paper) 100%);
    border: 1px solid #6b6b6b;
  }
  .edge-stripes {
    position: absolute; left: 0; top: 0; bottom: 0; width: 22px; display: flex;
  }
  .edge-stripes span { flex: 1; }
  .edge-stripes .s-navy { background: var(--navy); }
  .edge-stripes .s-blue { background: var(--blue); }
  .edge-stripes .s-sky { background: var(--sky); }
  .edge-stripes .s-sun { background: var(--sun); }
  .brand {
    position: absolute; left: 22px; right: 0; top: 246px;
    display: flex; align-items: center; justify-content: center; gap: 16px;
    color: var(--navy); font-weight: 700;
  }
  .brand-mark { width: 44px; height: 44px; background: var(--sun); }
  .brand-name { font-size: 86px; line-height: 1; letter-spacing: 0; }
  .brand-tagline {
    position: absolute; left: 22px; right: 0; top: 359px; text-align: center;
    color: var(--sky); font-weight: 700; font-size: 19px; letter-spacing: 11px;
    text-indent: 11px;
  }
  .card-back {
    top: 621px; background: var(--navy); color: var(--white); text-align: center;
  }
  .person-name {
    position: absolute; left: 0; right: 0; top: 161px;
    font-size: 38px; font-weight: 700; letter-spacing: 0.3px;
  }
  .divider {
    position: absolute; left: 204px; top: 232px; width: 467px; height: 36px;
  }
  .contact {
    position: absolute; left: 0; right: 0; font-size: 27px; font-weight: 500;
  }
  .contact-phone { top: 301px; }
  .contact-email { top: 343px; }
</style>
</head>
<body>
  <section class="card card-front">
    <div class="edge-stripes">
      <span class="s-navy"></span><span class="s-blue"></span><span class="s-sky"></span><span class="s-sun"></span>
    </div>
    <div class="brand">
      <span class="brand-mark"></span>
      <span class="brand-name">COPPERLEAF</span>
    </div>
    <div class="brand-tagline">MOTORIZED SHADES</div>
  </section>

  <section class="card card-back">
    <h1 class="person-name">NAME OF PERSON</h1>
    <svg class="divider" viewBox="0 0 467 36" aria-hidden="true">
      <line x1="0" y1="18" x2="172" y2="18" stroke="#00aeef" stroke-width="2"/>
      <line x1="295" y1="18" x2="467" y2="18" stroke="#00aeef" stroke-width="2"/>
      <circle cx="210" cy="18" r="16" fill="#ffffff"/>
      <path d="M203 10 l4 -1 l2 5 l-2.5 2 a10 10 0 0 0 5 5 l2 -2.5 l5 2 l-1 4 c-8 1 -16 -7 -14.5 -14.5z" fill="#00aeef"/>
      <circle cx="258" cy="18" r="16" fill="#ffffff"/>
      <rect x="248" y="11" width="20" height="14" fill="#00aeef"/>
      <path d="M248 11 l10 8 l10 -8 M248 25 l7 -7 M268 25 l-7 -7" stroke="#ffffff" stroke-width="1.3" fill="none"/>
    </svg>
    <p class="contact contact-phone">+919812340567</p>
    <p class="contact contact-email">info@cplmshades.com</p>
  </section>
</body>
</html>
```